BRISK Body Transformations

12 Week Fresh Start Programme

website preview (it's not live yet) :

http://exampletrainer.sitebuildhub.example/preview/7xqwbe.5lp8rt32mmqz7.a1942f8c60e527ab39147996cd8a457f

colour palette:

RGB codes:

Yellow : R 242,G 206,B 130.
Pink : R 248, G 149,B 133
Dark Pink : R 190,G 108,B 106
Blue : R 38.G 69,B 97#4
Grey : R 78,G 110,B 130

Target Market(s)

Female’s wanting to lose weight, sculpt muscle who are lacking in confidence and feel overwhelmed and don’t know where to start in improving their fitness and lifestyle

Font styles to use
Sans Serif

Colors
fee3d4
ffffff

Requirements
Must have
• My specific colour palette - see above

```html
<!DOCTYPE html>
<html lang="en">
<head>
<meta charset="utf-8">
<title>BRISK Body Transformations – 12 Week Fresh Start Programme</title>
<link rel="stylesheet" href="https://fonts.googleapis.com/css2?family=Montserrat:wght@400;500;600;700&family=Poppins:wght@500;600&display=swap">
<style>
  :root {
    --page-bg: #ece7e3;
    --flyer-dark: #2a2426;
    --flyer-dark-2: #342c2e;
    --yellow: #f2ce82;
    --pink: #f89585;
    --dark-pink: #be6c6a;
    --blue: #264561;
    --grey: #4e6e82;
    --cream: #fee3d4;
    --white: #ffffff;
    --ink: #1e1a1b;
  }
  * { box-sizing: border-box; margin: 0; padding: 0; }
  html, body { width: 1200px; height: 800px; overflow: hidden; }
  body {
    background: var(--page-bg);
    font-family: "Montserrat", sans-serif;
  }
  .flyer {
    position: absolute;
    left: 340px; top: 40px;
    width: 520px; height: 720px;
    background: radial-gradient(ellipse at 60% 40%, var(--flyer-dark-2), var(--flyer-dark) 70%);
    overflow: hidden;
    box-shadow: 0 10px 30px rgba(0,0,0,.25);
  }
  .brand {
    position: absolute;
    top: 52px; left: 0; width: 100%;
    text-align: center;
  }
  .brand-rule {
    display: block;
    width: 200px; height: 1px;
    margin: 0 auto 10px;
    background: var(--dark-pink);
  }
  .brand-name {
    font-family: "Montserrat", sans-serif;
    font-weight: 600;
    font-size: 44px;
    letter-spacing: 14px;
    padding-left: 14px;
    color: var(--pink);
    line-height: 1;
  }
  .brand-rule.bottom { margin: 12px auto 0; }
  .art { position: absolute; left: 0; top: 0; width: 520px; height: 720px; }
  .headline {
    position: absolute;
    right: 38px; top: 425px;
    text-align: right;
    color: var(--cream);
  }
  .headline-big {
    font-family: "Poppins", sans-serif;
    font-weight: 600;
    font-size: 72px;
    line-height: 1;
    letter-spacing: 1px;
  }
  .headline-box {
    display: inline-block;
    margin-top: 4px;
    padding: 3px 10px;
    background: var(--cream);
    color: var(--ink);
    font-weight: 700;
    font-size: 20px;
    line-height: 24px;
    text-transform: uppercase;
    letter-spacing: .5px;
  }
  .headline-sub {
    margin-top: 6px;
    font-weight: 500;
    font-size: 16px;
    line-height: 20px;
    letter-spacing: 9px;
    text-transform: uppercase;
  }
  .services {
    position: absolute;
    top: 566px; left: 150px;
    display: flex; gap: 40px;
  }
  .services ul { list-style: none; }
  .services li {
    color: var(--cream);
    font-size: 14px;
    line-height: 22px;
    display: flex; align-items: center; gap: 9px;
  }
  .services li::before {
    content: "";
    width: 10px; height: 10px;
    background: var(--cream);
    border-radius: 2px;
  }
  .contact {
    position: absolute;
    left: 20px; top: 646px;
    color: var(--ink);
  }
  .contact-phone { font-weight: 700; font-size: 16px; line-height: 20px; }
  .contact-line { font-size: 11px; line-height: 14px; margin-top: 4px; }
  .contact-line span { margin: 0 8px; }
</style>
</head>
<body>
  <main class="flyer">
    <svg class="art" viewBox="0 0 520 720">
      <defs>
        <linearGradient id="photoTone" x1="0" y1="0" x2="1" y2="0">
          <stop offset="0" stop-color="#be6c6a"/>
          <stop offset=".45" stop-color="#f89585"/>
          <stop offset="1" stop-color="#f2ce82"/>
        </linearGradient>
      </defs>
      <polygon class="photo-band" points="0,200 490,176 490,398 0,440" fill="url(#photoTone)"
               role="img" aria-label="Photo of a woman in sportswear doing a kneeling leg-raise exercise"/>
      <line class="band-rule" x1="60" y1="190" x2="250" y2="181" stroke="#fee3d4" stroke-width="2"/>
      <line class="band-rule" x1="300" y1="419" x2="500" y2="402" stroke="#fee3d4" stroke-width="2"/>
      <polygon class="contact-panel" points="0,585 0,720 500,720" fill="#ffffff"/>
    </svg>

    <header class="brand">
      <span class="brand-rule"></span>
      <div class="brand-name">BRISK</div>
      <span class="brand-rule bottom"></span>
    </header>

    <section class="headline">
      <div class="headline-big">12 WEEK</div>
      <div class="headline-box">Fresh Start</div>
      <div class="headline-sub">Programme</div>
    </section>

    <section class="services">
      <ul>
        <li>Weight Training</li>
        <li>Personal Training</li>
        <li>Yoga and Pilates</li>
      </ul>
      <ul>
        <li>Diet Nutrition</li>
        <li>Time Management</li>
        <li>Martial Arts</li>
      </ul>
    </section>

    <footer class="contact">
      <div class="contact-phone">Call (555) 014 2276</div>
      <div class="contact-line">48 Harbor Lane, Brookvale, BV 10412</div>
      <div class="contact-line">www.briskfit.example<span>|</span>info@briskfit.example</div>
    </footer>
  </main>
</body>
</html>
```